Grill, Tunes & Summer Feast.

I need an A3 Poster, Insta Square and Facebook Event Cover photo for a Grill Tunes and Feast Event. Details as follows:

Name: Grill, Tunes and Summer Feast
12pm - Late. Jan 26th at Tallow Creek Taphousing
Acts:
Tin Sparrow - 7pm
Copper Wire & Slow Morris - 3pm - 7pm
Derek Holloway - 12pm -3pm

Free BBQ 2-4pm.

```html
<!DOCTYPE html>
<html lang="en">
<head>
<meta charset="utf-8">
<title>Grill, Tunes &amp; Summer Feast – Event Set</title>
<link rel="stylesheet" href="https://fonts.googleapis.com/css2?family=Oswald:wght@400;500;600&display=swap">
<style>
  :root {
    --board: #e8e8e6;
    --navy: #1d2b3c;
    --navy-soft: #26364a;
    --white: #ffffff;
    --salmon: #d4776d;
    --shadow: rgba(0,0,0,0.18);
  }
  * { box-sizing: border-box; margin: 0; padding: 0; }
  html, body { width: 1099px; height: 1200px; overflow: hidden; }
  body {
    background: var(--board);
    font-family: "Oswald", "Arial Narrow", sans-serif;
    color: var(--white);
    position: relative;
  }
  .piece {
    position: absolute;
    background: var(--navy);
    box-shadow: 0 14px 14px -10px var(--shadow);
  }
  .event-cover { left: 130px; top: 121px; width: 839px; height: 311px; }
  .poster { left: 130px; top: 485px; width: 400px; height: 566px; }
  .square { left: 564px; top: 485px; width: 405px; height: 404px; }

  /* Circular event title */
  .event-title { position: absolute; overflow: visible; }
  .event-cover .event-title { left: 48px; top: 29px; width: 250px; height: 250px; }
  .poster .event-title { left: 32px; top: 32px; width: 334px; height: 334px; }
  .square .event-title { left: 82px; top: 20px; width: 240px; height: 240px; }
  .event-title text {
    font-family: "Oswald", "Arial Narrow", sans-serif;
    font-weight: 600;
    font-size: 36px;
    letter-spacing: 2px;
    fill: var(--white);
    text-transform: uppercase;
  }
  .title-art { fill: var(--navy-soft); }

  .divider { position: absolute; width: 1px; background: var(--white); }
  .event-cover .divider { left: 364px; top: 26px; height: 258px; }
  .poster .divider { left: 184px; top: 465px; height: 75px; }
  .square .divider { left: 184px; top: 315px; height: 67px; }

  .free-bbq {
    position: absolute;
    color: var(--salmon);
    font-weight: 400;
    text-align: center;
    white-space: nowrap;
  }
  .event-cover .free-bbq { left: 419px; width: 349px; top: 256px; font-size: 19px; }
  .poster .free-bbq { left: 0; width: 400px; top: 394px; font-size: 27px; }
  .square .free-bbq { left: 0; width: 405px; top: 273px; font-size: 20px; }

  /* Venue name */
  .brand {
    position: absolute;
    display: flex; flex-direction: column; align-items: center; justify-content: center;
    font-weight: 600; line-height: 1; text-transform: uppercase;
  }
  .brand-main { letter-spacing: 0.5px; text-align: center; }
  .brand-sub { letter-spacing: 3px; margin-top: 4px; }
  .brand-tab {
    left: 519px; top: 0; width: 148px; height: 89px;
    background: var(--white);
    clip-path: polygon(0 0,100% 0,100% 100%,50% 90%,0 100%);
    color: var(--navy);
    padding-bottom: 8px;
  }
  .brand-tab .brand-main { font-size: 22px; }
  .brand-tab .brand-sub { font-size: 10px; }
  .poster .brand { left: 26px; top: 466px; width: 144px; }
  .square .brand { left: 22px; top: 314px; width: 144px; }
  .poster .brand-main, .square .brand-main { font-size: 27px; line-height: 1; }
  .poster .brand-sub, .square .brand-sub { font-size: 11px; margin-top: 5px; }

  .details { position: absolute; font-weight: 400; white-space: nowrap; }
  .when { line-height: 1; text-align: center; letter-spacing: -0.3px; }
  .where { display: flex; align-items: center; gap: 0.7em; line-height: 1.2; }
  .where::before, .where::after { content: ""; flex: 1; height: 1px; background: var(--white); }
  .acts { display: flex; align-items: center; }
  .acts-label { margin-right: 0.9em; }
  .acts-list { list-style: none; }
  .acts-list li { line-height: 1.3; }
  .acts-list li::before { content: "\266B"; margin-right: 0.4em; }

  .event-cover .details { left: 448px; top: 105px; width: 300px; }
  .event-cover .when { font-size: 42px; }
  .event-cover .where { font-size: 18px; margin-top: 6px; }
  .event-cover .acts { margin-top: 10px; }
  .event-cover .acts-label { font-size: 27px; }
  .event-cover .acts-list { font-size: 16.5px; }

  .poster .details { left: 208px; top: 468px; width: 163px; }
  .poster .when { font-size: 23px; }
  .poster .where { font-size: 9.5px; margin-top: 3px; }
  .poster .acts { margin-top: 8px; }
  .poster .acts-label { font-size: 13px; margin-right: 0.6em; }
  .poster .acts-list { font-size: 8.3px; }

  .square .details { left: 223px; top: 318px; width: 145px; }
  .square .when { font-size: 20px; }
  .square .where { font-size: 8.5px; margin-top: 3px; }
  .square .acts { margin-top: 6px; }
  .square .acts-label { font-size: 11px; margin-right: 0.6em; }
  .square .acts-list { font-size: 7.4px; }
</style>
</head>
<body>

<svg width="0" height="0" style="position:absolute" aria-hidden="true">
  <defs>
    <path id="arc-top" d="M 30,128 A 90 90 0 0 1 210,128"/>
    <path id="arc-bottom" d="M 8,112 A 112 112 0 0 0 232,112"/>
  </defs>
</svg>

<section class="piece event-cover" aria-label="Facebook event cover">
  <svg class="event-title" viewBox="0 0 240 240" aria-label="Grill, Tunes &amp; Summer Feast">
    <circle class="title-art" cx="120" cy="120" r="60" role="img" aria-label="Sketches of a speaker, guitar, microphone, beer mug and grill"/>
    <text text-anchor="middle"><textPath href="#arc-top" startOffset="50%">Grill, Tunes</textPath></text>
    <text text-anchor="middle"><textPath href="#arc-bottom" startOffset="50%">&amp; Summer Feast</textPath></text>
  </svg>
  <div class="divider"></div>
  <div class="brand brand-tab">
    <span class="brand-main">Tallow Creek</span>
    <span class="brand-sub">Taphouse</span>
  </div>
  <div class="details">
    <p class="when">12pm - Late. Jan 26th</p>
    <p class="where">at Tallow Creek Taphousing</p>
    <div class="acts">
      <span class="acts-label">ACTS:</span>
      <ul class="acts-list">
        <li>Tin Sparrow - 7pm</li>
        <li>Copper Wire &amp; Slow Morris - 3pm - 7pm</li>
        <li>Derek Holloway - 12pm - 3pm</li>
      </ul>
    </div>
  </div>
  <p class="free-bbq">Free BBQ 2-4pm</p>
</section>

<section class="piece poster" aria-label="A3 poster">
  <svg class="event-title" viewBox="0 0 240 240" aria-label="Grill, Tunes &amp; Summer Feast">
    <circle class="title-art" cx="120" cy="120" r="60" role="img" aria-label="Sketches of a speaker, guitar, microphone, beer mug and grill"/>
    <text text-anchor="middle"><textPath href="#arc-top" startOffset="50%">Grill, Tunes</textPath></text>
    <text text-anchor="middle"><textPath href="#arc-bottom" startOffset="50%">&amp; Summer Feast</textPath></text>
  </svg>
  <p class="free-bbq">Free BBQ 2-4pm</p>
  <div class="brand">
    <span class="brand-main">Tallow<br>Creek</span>
    <span class="brand-sub">Taphouse</span>
  </div>
  <div class="divider"></div>
  <div class="details">
    <p class="when">12pm - Late. Jan 26th</p>
    <p class="where">at Tallow Creek Taphousing</p>
    <div class="acts">
      <span class="acts-label">ACTS:</span>
      <ul class="acts-list">
        <li>Tin Sparrow - 7pm</li>
        <li>Copper Wire &amp; Slow Morris - 3pm - 7pm</li>
        <li>Derek Holloway - 12pm - 3pm</li>
      </ul>
    </div>
  </div>
</section>

<section class="piece square" aria-label="Instagram square">
  <svg class="event-title" viewBox="0 0 240 240" aria-label="Grill, Tunes &amp; Summer Feast">
    <circle class="title-art" cx="120" cy="120" r="60" role="img" aria-label="Sketches of a speaker, guitar, microphone, beer mug and grill"/>
    <text text-anchor="middle"><textPath href="#arc-top" startOffset="50%">Grill, Tunes</textPath></text>
    <text text-anchor="middle"><textPath href="#arc-bottom" startOffset="50%">&amp; Summer Feast</textPath></text>
  </svg>
  <p class="free-bbq">Free BBQ 2-4pm</p>
  <div class="brand">
    <span class="brand-main">Tallow<br>Creek</span>
    <span class="brand-sub">Taphouse</span>
  </div>
  <div class="divider"></div>
  <div class="details">
    <p class="when">12pm - Late. Jan 26th</p>
    <p class="where">at Tallow Creek Taphousing</p>
    <div class="acts">
      <span class="acts-label">ACTS:</span>
      <ul class="acts-list">
        <li>Tin Sparrow - 7pm</li>
        <li>Copper Wire &amp; Slow Morris - 3pm - 7pm</li>
        <li>Derek Holloway - 12pm - 3pm</li>
      </ul>
    </div>
  </div>
</section>

</body>
</html>
```